Letter Head Design

I need a letter head design based on my company logo that I attached.
Include phone number: (403)582-4316
Address: 347 14th Avenue NE, Calgary, Alberta, Canada, T3K 4R8

Industry/Entity Type

It Company

```html
<!DOCTYPE html>
<html lang="en">
<head>
<meta charset="utf-8">
<title>Brightvale Interiors Corp. — Letterhead</title>
<link rel="stylesheet" href="https://fonts.googleapis.com/css2?family=Open+Sans:wght@400;600&family=EB+Garamond:wght@400&display=swap">
<style>
  :root {
    --page: #ffffff;
    --brand-blue: #1d5fb0;
    --band-top: #2a6cc0;
    --band-bottom: #123f86;
    --brand-green: #58b247;
    --mark-soft: #d6e4f3;
    --ink: #1e2a3a;
  }
  * { margin: 0; padding: 0; box-sizing: border-box; }
  html, body { width: 936px; height: 1200px; overflow: hidden; background: var(--page); }
  .letterhead {
    position: relative;
    width: 936px;
    height: 1200px;
    background: var(--page);
    font-family: "Open Sans", Arial, sans-serif;
    color: var(--ink);
  }
  .masthead {
    position: absolute;
    top: 36px;
    left: 0;
    width: 100%;
    display: flex;
    flex-direction: column;
    align-items: center;
    gap: 22px;
  }
  .masthead__square {
    width: 120px;
    height: 120px;
    border-radius: 10px;
    background: var(--brand-blue);
  }
  .masthead__name {
    font-size: 34px;
    font-weight: 600;
    color: var(--brand-blue);
    letter-spacing: -0.5px;
  }
  .footer-square {
    position: absolute;
    left: 18px;
    top: 1063px;
    width: 117px;
    height: 117px;
    border-radius: 8px;
    background: var(--mark-soft);
  }
  .tagline-band {
    position: absolute;
    left: 153px;
    right: 0;
    top: 1086px;
    height: 66px;
    border-top: 2px solid var(--brand-green);
    border-bottom: 2px solid var(--brand-green);
    padding: 5px 0 3px;
    overflow: hidden;
  }
  .tagline-band__bar {
    height: 100%;
    background: linear-gradient(to bottom, var(--band-top), var(--band-bottom));
    display: flex;
    align-items: center;
    justify-content: flex-end;
    padding-right: 22px;
  }
  .tagline {
    font-family: "EB Garamond", Georgia, serif;
    font-size: 28px;
    color: #ffffff;
    letter-spacing: 0.5px;
    white-space: nowrap;
  }
  .contact {
    position: absolute;
    right: 26px;
    top: 1160px;
    display: flex;
    align-items: center;
    gap: 6px;
    font-size: 18px;
    color: var(--ink);
    white-space: nowrap;
  }
  .contact__item { display: flex; align-items: center; gap: 5px; }
  .contact__item + .contact__item { margin-left: 8px; }
  .contact__icon { width: 14px; height: 18px; fill: var(--brand-blue); }
</style>
</head>
<body>
  <main class="letterhead">
    <header class="masthead">
      <div class="masthead__square"></div>
      <div class="masthead__name">Brightvale Interiors Corp.</div>
    </header>

    <footer>
      <div class="footer-square"></div>
      <div class="tagline-band">
        <div class="tagline-band__bar">
          <span class="tagline">Crafted With You in Mind</span>
        </div>
      </div>
      <address class="contact" style="font-style: normal;">
        <span class="contact__item">
          <svg class="contact__icon" viewBox="0 0 14 18" aria-hidden="true">
            <path d="M3 2 L5.5 1.5 L7 5 L5.3 6.3 C6 8.6 7.3 10.3 9 11.4 L10.4 9.8 L13.5 11.6 L12.8 14.2 C12.5 15 11.6 15.4 10.8 15.2 C6.2 13.8 2.6 9.6 1.6 4.6 C1.5 3.4 2 2.4 3 2 Z"/>
          </svg>
          (403)582-4316
        </span>
        <span class="contact__item">
          <svg class="contact__icon" viewBox="0 0 14 18" aria-hidden="true">
            <path d="M7 1 C3.7 1 1.5 3.4 1.5 6.4 C1.5 10.4 7 17 7 17 C7 17 12.5 10.4 12.5 6.4 C12.5 3.4 10.3 1 7 1 Z M7 8.6 A2.2 2.2 0 1 1 7 4.2 A2.2 2.2 0 1 1 7 8.6 Z"/>
          </svg>
          347 14th Avenue NE, Calgary, Alberta, Canada, T3K 4R8
        </span>
      </address>
    </footer>
  </main>
</body>
</html>
```